Redesign B2B website

We are redesigning/ restructuring our current website. We provide company feedback surveys. We claim to be market leader in our country.
We like to be seen as a trustworthy, reliable and innovative partner to the top 1500 companies in the netherlands.
We want to be seen as a personal company.
Current website http://www.quorvane.nl does not meet our standards mentioned above.
Updates
Added Homepage layout. Please check
Target Market(s)
Large businesses, HR, decisiontakers
Industry/Entity Type
It Company
Requirements
Must have
- -The website is intended to be responsive. please take that into account. (propose plankit.es)
-The design should match our Style colors(will be provided)
- Wireframes are provided. Fonts used are Open Sans and Esteban,. Feel free to change things around.
Nice to have
- We like the design to be "flat", not much 3d effects, or icons.
Minimalist, Wordpress style or Metro style.

```html
<!DOCTYPE html>
<html lang="nl">
<head>
<meta charset="utf-8">
<title>Quorvane – homepage</title>
<link href="https://fonts.googleapis.com/css2?family=Ubuntu:wght@400;500;700&display=swap" rel="stylesheet">
<style>
:root{
  --stage:#e6e6e6;
  --page:#ecebe9;
  --white:#ffffff;
  --yellow:#fdd22b;
  --orange:#f9a62f;
  --orange-dark:#f08a1c;
  --teal:#12aaa9;
  --teal-dark:#0c7773;
  --teal-light:#8ccac7;
  --nav-grey:#e3e6e6;
  --nav-text:#2f8db8;
  --grey-text:#7d7d6f;
}
*{box-sizing:border-box;margin:0;padding:0}
html,body{width:1200px;height:848px;overflow:hidden;background:var(--stage);font-family:"Ubuntu",sans-serif}
.site{position:absolute;left:257px;top:78px;width:686px;height:692px;background:var(--page);overflow:hidden;box-shadow:0 2px 6px rgba(0,0,0,.25)}
.abs{position:absolute}

/* header */
.header-white{left:0;top:0;width:248px;height:78px;background:var(--white)}
.header-yellow{left:248px;top:0;width:438px;height:78px;background:var(--yellow);border-bottom-left-radius:22px}
.brand-name{left:24px;top:24px;width:210px;height:30px;font-weight:500;font-size:24px;line-height:30px;color:var(--nav-text);text-align:left}
.utility{left:274px;top:22px;font-size:10px;color:var(--grey-text);white-space:nowrap}
.search{left:452px;top:40px;width:189px;height:27px;background:var(--white)}
.search svg{position:absolute;left:6px;top:5px}

/* nav */
.band-teal{left:0;top:78px;width:686px;height:21px;background:var(--teal-light)}
.band-line{left:0;top:93px;width:686px;height:5px;background:var(--teal-dark)}
.band-under{left:0;top:160px;width:686px;height:24px;background:var(--teal-light)}
.home-glow{left:55px;top:82px;width:140px;height:100px;border-radius:50%;background:var(--yellow)}
.nav{left:0;top:103px;width:686px;height:64px;background:linear-gradient(#f4f5f5,var(--nav-grey));border-radius:30px;box-shadow:inset 0 -3px 4px rgba(0,0,0,.06)}
.nav-home{left:63px;top:110px;width:120px;height:60px;background:linear-gradient(var(--teal),#0e9a98);border-radius:16px 16px 4px 4px;border:2px solid #3fc4c2;color:var(--white);font-size:12px;font-weight:500;display:flex;align-items:center;justify-content:center}
.nav-item{top:126px;color:var(--nav-text);font-size:11px;font-weight:500;text-align:center;line-height:13px;transform:translateX(-50%);white-space:nowrap}

/* body decoration */
.bg-shapes{left:0;top:184px;width:686px;height:508px;background:radial-gradient(circle at 40% 55%,#dcdbd8 0,#e7e6e3 40%,var(--page) 70%)}
.bg-tiles{left:270px;top:410px;width:416px;height:282px;background:linear-gradient(160deg,rgba(253,210,43,0) 20%,rgba(253,210,43,.45) 60%,rgba(253,210,43,.25))}

/* intro */
.band-yellow{left:0;top:286px;width:686px;height:128px;background:var(--yellow);border-radius:18px 0 0 18px}
.bubble{background:var(--teal);color:var(--white);font-size:10px;line-height:12px;border-radius:30px}
.intro{left:51px;top:297px;width:415px;height:105px;padding:12px 14px}
.intro ul{list-style:none;margin-top:10px}
.intro li{padding-left:10px;position:relative}
.intro li::before{content:"";position:absolute;left:0;top:3px;width:6px;height:6px;border-radius:50%;background:var(--yellow)}
.insight{left:184px;top:421px;width:414px;height:106px;padding:18px 10px 0 18px}

/* login */
.login{left:480px;top:195px;width:179px;height:162px;background:linear-gradient(var(--orange),var(--orange-dark));border:3px solid #f3e9d4;border-radius:12px}
.tab{top:-6px;width:52px;height:22px;border-radius:4px;font-size:9px;display:flex;align-items:center;justify-content:center;color:#555}
.tab-login{left:28px;background:var(--orange);border:2px solid #f7c78a}
.tab-register{left:92px;background:linear-gradient(#e2e2e2,#b8b8b8);border:1px solid #999}
.label{left:22px;font-size:9px;color:#5a3a10}
.field{left:22px;width:130px;height:18px;background:linear-gradient(#fff,#ececec);border-radius:8px}
.remember{left:20px;top:130px;font-size:9px;color:#5a3a10;display:flex;align-items:center;gap:4px}
.remember span{width:11px;height:11px;border-radius:50%;background:var(--white)}
.btn{height:16px;border-radius:3px;background:linear-gradient(#eee,#c9c9c9);font-size:9px;color:#555;display:flex;align-items:center;padding-left:4px}
.btn i{margin-left:auto;width:12px;height:16px;background:var(--orange);display:flex;align-items:center;justify-content:center}
.login .btn{left:106px;top:128px;width:48px}

/* newsletter */
.news{left:345px;top:558px;width:312px;height:89px;border-radius:12px;overflow:hidden;background:var(--white);box-shadow:0 0 0 3px #f3efe6}
.news-side{left:217px;top:0;width:95px;height:89px;background:linear-gradient(var(--orange),var(--orange-dark));border-left:3px solid #e07c10}
.news-title{left:26px;top:12px;font-size:10px;color:#666}
.news-field{left:58px;top:46px;width:142px;height:18px;background:linear-gradient(#fafafa,#e6e6e6);border-radius:9px}
.news .btn{left:234px;top:48px;width:54px}
</style>
</head>
<body>
<main class="site">
  <div class="abs header-white"></div>
  <div class="abs header-yellow"></div>
  <p class="abs brand-name">Quorvane</p>
  <p class="abs utility">Select your language | voorlichting 020 4817263 | helpdesk 0800 5550192 | sitemap</p>
  <div class="abs search">
    <svg width="18" height="18" viewBox="0 0 18 18"><circle cx="7" cy="7" r="5.5" fill="none" stroke="#1d5d8a" stroke-width="2"/><line x1="11" y1="11" x2="16.5" y2="16.5" stroke="#1d5d8a" stroke-width="2.5" stroke-linecap="round"/></svg>
  </div>

  <div class="abs band-teal"></div>
  <div class="abs home-glow"></div>
  <div class="abs band-line"></div>
  <div class="abs band-under"></div>
  <nav class="abs nav"></nav>
  <div class="abs nav-home">HOME</div>
  <span class="abs nav-item" style="left:240px;top:132px">ONZE KLANTEN</span>
  <span class="abs nav-item" style="left:349px;top:132px">NIEUWS</span>
  <span class="abs nav-item" style="left:451px">WERKEN<br>BIJ QUORVANE</span>
  <span class="abs nav-item" style="left:540px">OVER<br>QUORVANE</span>
  <span class="abs nav-item" style="left:624px;top:136px">CONTACT</span>

  <div class="abs bg-shapes" role="img" aria-label="Faint grey geometric shapes as background decoration"></div>
  <div class="abs bg-tiles" role="img" aria-label="Pattern of small yellow tiles"></div>

  <div class="abs band-yellow"></div>
  <section class="abs bubble intro">
    <p>Medewerkers- en klantenonderzoek<br>Geniet van de expertise van de marktleider. Quorvane is specialist op het gebied van:</p>
    <ul>
      <li>Medewerkersonderzoek: hoe staan medewerkers in de organisatie</li>
      <li>Klantenonderzoek: hoe ervaren klanten de dienstverlening</li>
      <li>Intern klantenonderzoek: hoe ervaren medewerkers (interne klanten)<br>de samenwerking met andere afdelingen</li>
    </ul>
  </section>

  <section class="abs login">
    <div class="abs tab tab-login">LOG IN</div>
    <div class="abs tab tab-register">REGISTER</div>
    <span class="abs label" style="top:46px">USERNAME</span>
    <div class="abs field" style="top:58px"></div>
    <span class="abs label" style="top:87px">PASSWORD</span>
    <div class="abs field" style="top:99px"></div>
    <div class="abs remember"><span></span>REMEMBER ME</div>
    <div class="abs btn">LOG IN<i><svg width="6" height="8"><path d="M0 0L6 4L0 8Z" fill="#fff"/></svg></i></div>
  </section>

  <section class="abs bubble insight">
    <p>Met behulp van Quorvane's essentiële inzichten verbetert uw organisatie zichtbaar. Profiteer van onze doordachte concepten en praktische ondersteuning voor de follow-up in uw organisatie. Met aantrekkelijk vormgegeven enquêtes, toegankelijke rapportages en uitgebreide benchmarkmogelijkheden maken we uw succes meetbaar. U geniet daarbij van de energieke, professionele begeleiding van onze medewerkers. Onze dienstverlening wordt door onze klanten beoordeeld met een ruime 8,5!</p>
  </section>

  <section class="abs news">
    <span class="abs news-title">Subscribe to Newsletter</span>
    <svg class="abs" style="left:14px;top:44px" width="36" height="20" viewBox="0 0 36 20"><line x1="0" y1="8" x2="9" y2="8" stroke="#f08a1c" stroke-width="1.5"/><line x1="3" y1="13" x2="9" y2="13" stroke="#f08a1c" stroke-width="1.5"/><rect x="11" y="3" width="22" height="15" rx="2" fill="#f9a62f"/><path d="M11 4L22 12L33 4" fill="none" stroke="#fff" stroke-width="1.2"/></svg>
    <div class="abs news-field"></div>
    <div class="abs news-side"></div>
    <div class="abs btn">submit<i><svg width="6" height="8"><path d="M0 0L6 4L0 8Z" fill="#fff"/></svg></i></div>
  </section>
</main>
</body>
</html>
```